Redesign Business Cards, Attached

Please read instructions carefully. If you have any questions send a message before submitting your ONE design. Please redesign attached business cards. Double sided. Use same content and descriptions. Use black, silver, crimson red and gold colors. My only issue with the attached design is the background colors. I like the layout as-is. I can provide the individual pictures on the back side later. Do not submit more than one design. One submission shall include both front and back. Do not submit front and back separately. A second project will be launched to create a matching post card after completion of this.
Industry/Entity Type
see description and attachments.
Contact Information for Business Card
Requirements
Must have
- see description and attachments.
Nice to have
Should not have

```html
<!DOCTYPE html>
<html lang="en">
<head>
<meta charset="utf-8">
<title>Halvers Boat School – Business Card</title>
<link rel="stylesheet" href="https://fonts.googleapis.com/css2?family=Lato:wght@400;700&family=Arimo:wght@400&display=swap">
<style>
  :root {
    --backdrop: #a5804a;
    --black: #050506;
    --gold: #f6c556;
    --crimson: #b5141c;
    --crimson-deep: #8a0c12;
    --tile: #1f1d1e;
    --white: #ffffff;
    --seal: #3a1512;
  }
  * { margin: 0; padding: 0; box-sizing: border-box; }
  html, body { width: 1200px; height: 1154px; overflow: hidden; }
  body { background: var(--backdrop); position: relative; font-family: "Arimo", Arial, sans-serif; }

  .card {
    position: absolute; left: 250px; width: 700px; height: 400px; overflow: hidden;
    box-shadow: 12px 12px 10px rgba(60, 40, 15, 0.45);
  }
  .card--front { top: 181px; background: var(--black); }
  .card--back { top: 595px; }

  .seal-ring {
    position: absolute; left: -1px; top: 70px; width: 260px; height: 260px;
    border-radius: 50%; border: 22px solid var(--seal); opacity: 0.9;
  }
  .front-photo { position: absolute; inset: 0; }

  .name-frame {
    position: absolute; left: 110px; top: 210px; width: 470px; height: 55px;
    border: 1.5px solid var(--gold); border-right: none;
  }
  .name {
    position: absolute; left: 124px; top: 212px;
    font-family: "Lato", sans-serif; font-weight: 700; font-size: 42px;
    color: var(--gold); letter-spacing: 0.5px; white-space: nowrap;
  }
  .title {
    position: absolute; left: 111px; top: 272px;
    font-size: 17px; letter-spacing: 1.6px; color: var(--white); white-space: nowrap;
  }

  .contact { position: absolute; left: 239px; height: 21px; display: flex; align-items: center; }
  .contact--email { top: 310px; }
  .contact--web { top: 338px; }
  .contact-icon {
    width: 21px; height: 21px; background: var(--gold);
    display: flex; align-items: center; justify-content: center;
  }
  .contact-bar {
    margin-left: 3px; height: 21px; background: var(--crimson);
    clip-path: polygon(0 0, 100% 0, 93% 100%, 0 100%);
    font-family: "Lato", sans-serif; font-size: 19px; line-height: 21px;
    color: var(--gold); padding-left: 5px; white-space: nowrap;
  }
  .contact--email .contact-bar { width: 250px; }
  .contact--web .contact-bar { width: 232px; }

  .back-photo { position: absolute; inset: 0; }

  .brand { position: absolute; left: 0; right: 0; top: 40px; text-align: center; }
  .brand-dot {
    width: 62px; height: 62px; border-radius: 50%; background: var(--white);
    margin: 0 auto 8px;
  }
  .brand-name {
    font-family: "Arimo", sans-serif; font-size: 16px; letter-spacing: 1.5px;
    color: var(--white);
  }

  .services {
    position: absolute; left: 47px; top: 181px;
    display: grid; grid-template-columns: repeat(4, 140px); grid-auto-rows: 62px;
    column-gap: 15px; row-gap: 14px;
  }
  .service {
    background: var(--tile); border-radius: 5px; color: var(--white);
    display: flex; align-items: center; justify-content: center; text-align: center;
    font-size: 17px; line-height: 15px; letter-spacing: 1.4px; padding: 0 4px;
  }
  .service--small { font-size: 15px; line-height: 13.5px; letter-spacing: 1px; }

  .back-web {
    position: absolute; left: 0; right: 0; top: 346px; text-align: center;
    font-family: "Lato", sans-serif; font-size: 29px; color: var(--gold);
  }
</style>
</head>
<body>

<section class="card card--front">
  <div class="seal-ring"></div>
  <svg class="front-photo" width="700" height="400" viewBox="0 0 700 400" role="img" aria-label="Photo of a motor boat cruising over sparkling water, sepia toned">
    <defs>
      <linearGradient id="sepia" x1="0" y1="0" x2="1" y2="1">
        <stop offset="0" stop-color="#cfc3aa"/>
        <stop offset="0.5" stop-color="#6e6350"/>
        <stop offset="1" stop-color="#2a241b"/>
      </linearGradient>
    </defs>
    <polygon points="700,0 700,400 460,400" fill="url(#sepia)"/>
  </svg>

  <div class="name-frame"></div>
  <div class="name">JORDAN T. HALVERS</div>
  <div class="title">USCG Licensed Captain Certified Instructor</div>

  <div class="contact contact--email">
    <span class="contact-icon">
      <svg width="15" height="11" viewBox="0 0 15 11"><rect x="0.75" y="0.75" width="13.5" height="9.5" fill="none" stroke="#1a1a1a" stroke-width="1.2"/><polyline points="0.75,0.75 7.5,6 14.25,0.75" fill="none" stroke="#1a1a1a" stroke-width="1.2"/></svg>
    </span>
    <span class="contact-bar">service@helmready.com</span>
  </div>
  <div class="contact contact--web">
    <span class="contact-icon">
      <svg width="14" height="14" viewBox="0 0 14 14" fill="none" stroke="#1a1a1a" stroke-width="1"><circle cx="7" cy="7" r="6"/><ellipse cx="7" cy="7" rx="2.6" ry="6"/><line x1="1" y1="7" x2="13" y2="7"/><line x1="2" y1="4" x2="12" y2="4"/><line x1="2" y1="10" x2="12" y2="10"/></svg>
    </span>
    <span class="contact-bar">www.HelmReady.com</span>
  </div>
</section>

<section class="card card--back">
  <svg class="back-photo" width="700" height="400" viewBox="0 0 700 400" role="img" aria-label="Photo of a sailboat deck and rigging with hills across the water, tinted crimson">
    <defs>
      <linearGradient id="crimson" x1="0" y1="0" x2="0" y2="1">
        <stop offset="0" stop-color="#96111a"/>
        <stop offset="0.45" stop-color="#7c0f14"/>
        <stop offset="1" stop-color="#a3151c"/>
      </linearGradient>
    </defs>
    <rect width="700" height="400" fill="url(#crimson)"/>
  </svg>

  <div class="brand">
    <div class="brand-dot"></div>
    <div class="brand-name">Halvers Boat School</div>
  </div>

  <div class="services">
    <div class="service">Hands-On Boat Training</div>
    <div class="service">Introduction to Power boating</div>
    <div class="service">Precision Docking &amp; Boat Handling</div>
    <div class="service">Open Water Boat Handling</div>
    <div class="service">Island Anchoring</div>
    <div class="service">Open Water Advanced Maneuvers</div>
    <div class="service">Coastal Navigating</div>
    <div class="service service--small">Capaining/ Piloting Service for Your Outing</div>
  </div>

  <div class="back-web">www.HelmReady.com</div>
</section>

</body>
</html>
```